Web Design Project

I'm seeking a web designer that will design an elegant website for my Online Portfolio
I myself am a graphic designer, But web isn't my prime field. Ill need it to be
User interface friendly with zero complexity. I will provide all the files needed, and will also
Contribute to the graphics if needed. 3D style gallery feature would be nice but not essential
giving the website look a more virtual feel to its design feature. The overall design must have a multi-tech feel to it
but nothing overboard keeping it simple. Just be creative ;-)

THIS IS A CODED WEB SITE NOT ONLY DESIGN!!!

A quick intro would be nice, no more than 5 seconds using my logo and font and some of my designs.
My designs are mostly interface audio players and digital designs.
I am looking forward for a long term collaboration,as I will constantly need an update on my website.so its not
a one off thing.

Anything you need to add that I have forgot e-mail me!

•website must be php dynamic data base.
•colour scheme:Dark Grey,black,Blue, white,
•Ill be taking a new photo,this one is only an example to work on.

Examples:

http://morvtask0417.pixelvault.example/art/sorrento-lute-new-desgin-517390421
http://pelurin.pixelvault.example/art/52-Studio-406217935
http://tobrak3ft.pixelvault.example/art/Tobrakraft-2013-572038814
http://pelurin.pixelvault.example/art/Personal-Portfolio-V1-863025417

Links for the files:

http://www.filecrate.example/zip/x42m806q/About.html
http://www.filecrate.example/zip/7HWLK3zd/Vexilune_font__logo.html
http://www.filecrate.example/zip/RbkkPgaW/Portfolio.html
http://www.filecrate.example/zip/JtwnuEes/Resources.html
http://www.filecrate.example/zip/dHZcyrpf/Example_Photo.html

Target Market(s)

Design companies to be able to click onto the link of my website and see a nice design set up for my portfolio.

Industry/Entity Type

Digital

Requirements
Must have
• Be creative
Nice to have
• A short intro
3D gallery,simple style navigation,nothing ultra complicated.
Should not have
• 1)Any pictures of any kind of anyone else's art work, except if you include an abstract image having no complications with copyrights as you should know.
2)No music
3)lots of colours no more than 4 colours maximum 6 colour layout.

```html
<!DOCTYPE html>
<html lang="en">
<head>
<meta charset="utf-8">
<title>Vexilune — Portfolio</title>
<link rel="stylesheet" href="https://fonts.googleapis.com/css2?family=Raleway:wght@300;400;500&family=Open+Sans:wght@400&display=swap">
<style>
:root{
  --ink:#000;
  --paper:#fff;
  --canvas:#eceef2;
  --blue:#2a9fd0;
  --grey:#7d7d7d;
  --muted:#b9b9c4;
  --date:#a9b3cc;
}
*{margin:0;padding:0;box-sizing:border-box}
html,body{width:995px;height:1200px;overflow:hidden;background:var(--paper);font-family:"Open Sans",sans-serif}
.site-header{height:98px;border-bottom:1px solid #e3e4e8;position:relative}
.brand{position:absolute;left:47px;top:35px;font-family:"Raleway",sans-serif;font-weight:500;font-size:33px;color:var(--grey)}
.main-nav a{position:absolute;top:46px;font-family:"Raleway",sans-serif;font-size:21px;color:var(--blue);text-decoration:none}
.gallery{background:var(--canvas);height:938px;padding:35px 0 0 86px}
.grid{display:grid;grid-template-columns:repeat(4,192px);grid-template-rows:repeat(3,274px);column-gap:16px;row-gap:16px}
.card{position:relative;background:var(--ink);color:var(--paper);overflow:hidden}
.card.wide{grid-column:span 2}
.card.light{background:var(--paper);color:#111}
.media{height:132px;width:100%}
.card h3{font-family:"Raleway",sans-serif;font-weight:500;font-size:12.5px;line-height:13px;letter-spacing:-0.2px;margin:21px 14px 0}
.card p{font-size:8px;line-height:14px;color:#ccc;margin:8px 14px 0}
.card.light p{color:#8a8a8a}
.date{position:absolute;left:14px;bottom:11px;font-size:7.5px;color:var(--date)}
.card.light .date{color:#999}
.corner{position:absolute;right:10px;top:11px}
.full{position:absolute;inset:0}
.tag{position:absolute;left:16px;top:17px;font-family:"Raleway",sans-serif;color:#000}
.tag span{background:var(--paper);padding:1px 2px;box-decoration-break:clone;-webkit-box-decoration-break:clone}
.card .statement{font-family:"Raleway",sans-serif;font-weight:300;font-size:20px;line-height:24px;color:#c9ccd6;margin:24px 14px 0}
.card .quote{font-family:"Raleway",sans-serif;font-weight:400;font-size:20px;line-height:24px;color:var(--paper);margin:24px 14px 0}
.card .quote-by{font-size:9.5px;line-height:14px;color:var(--date);margin:12px 14px 0}
.site-footer{position:relative;height:164px}
.footer-col{position:absolute;top:30px}
.footer-col h4{font-family:"Raleway",sans-serif;font-weight:400;font-size:17px;color:var(--grey)}
.footer-col a{display:block;font-family:"Raleway",sans-serif;font-size:10.5px;color:var(--blue);text-decoration:none;margin-top:2px}
.socials{display:flex;gap:9px;margin-top:12px}
.socials span{width:15px;height:15px;border-radius:50%;background:var(--grey)}
</style>
</head>
<body>
<header class="site-header">
  <div class="brand">Vexilune</div>
  <nav class="main-nav">
    <a href="#" style="left:523px">Home</a>
    <a href="#" style="left:611px">About</a>
    <a href="#" style="left:714px">Portfolio</a>
    <a href="#" style="left:834px;top:50px">Reach me</a>
  </nav>
</header>

<main class="gallery">
  <div class="grid">
    <article class="card wide">
      <div class="full" role="img" aria-label="Photo of an empty road winding through orange mountain valley under storm clouds" style="background:linear-gradient(180deg,#2b2426 0%,#4a3a34 30%,#9a5a25 50%,#6a4a30 65%,#3c3a3a 100%)"></div>
      <div class="tag" style="font-size:25px"><span>Storm</span></div>
      <svg class="corner" width="22" height="9" viewBox="0 0 22 9" fill="#ccc"><polygon points="4,0 5.2,3 8.5,3 6,5 7,8.5 4,6.5 1,8.5 2,5 -0.5,3 2.8,3"/><rect x="12" y="0.5" width="9" height="8" fill="none" stroke="#ccc"/><polygon points="13,7.5 16,4 20,7.5"/></svg>
      <span class="date">February 6, 2013</span>
    </article>

    <article class="card light">
      <div class="media" role="img" aria-label="Black and white portrait photo of a man" style="background:linear-gradient(180deg,#f4f4f4,#8f8f8f)"></div>
      <h3>Behind the scene: Marc Delorme</h3>
      <p>Marc is a technology entrepreneur with +10 years's business background currently located in the heart of Canada.</p>
      <span class="date">February 2, 2013</span>
    </article>

    <article class="card">
      <svg class="corner" width="10" height="9" viewBox="0 0 10 9" fill="#ccc"><polygon points="0,3 3,3 8,0 8,9 3,6 0,6"/></svg>
      <p class="statement">We see it as our responsibility to keep the web moving forwards.</p>
      <span class="date">February 21, 2013</span>
    </article>

    <article class="card">
      <div class="media" role="img" aria-label="Black and white photo of a blues guitarist singing on stage" style="background:linear-gradient(160deg,#111,#555 60%,#222)"></div>
      <h3>Ray Talbot</h3>
      <p>Raymond J. Talbot (born March 4, 1931), known by the stage name Ray Talbot, is an American blues guitarist and singer-songwriter.</p>
      <span class="date">February 20, 2013</span>
    </article>

    <article class="card">
      <div class="media" role="img" aria-label="Photo of a foggy city street at night with streetlights" style="background:linear-gradient(180deg,#222,#6a6a6a 55%,#2c2c2c)"></div>
      <h3>Inspiring ideas to enhance human experience</h3>
      <p>In a nunc quam, ac ullamcorper felis. Cras ante arcu, dapibus vitae tristique sit amet, porta non nisi.</p>
      <span class="date">February 12, 2013</span>
    </article>

    <article class="card">
      <svg class="corner" width="10" height="8" viewBox="0 0 10 8" fill="#ccc"><rect x="0" y="0" width="4" height="4"/><rect x="5.5" y="0" width="4" height="4"/><rect x="2" y="3" width="1.5" height="4"/><rect x="7.5" y="3" width="1.5" height="4"/></svg>
      <p class="quote">“Those who mind don't matter, and those who matter don't mind.”</p>
      <p class="quote-by">— Theo Marsh</p>
      <span class="date">February 9, 2013</span>
    </article>

    <article class="card">
      <div class="media" role="img" aria-label="Photo of a crimson flower on a black background" style="background:radial-gradient(circle at 45% 45%,#c23c70 0%,#6a1a3a 30%,#000 62%)"></div>
      <h3>Oxyde Noir</h3>
      <p>It is a long established fact that a reader will be distracted by the readable content of a page when looking at its layout.</p>
      <span class="date">February 2, 2013</span>
    </article>

    <article class="card">
      <div class="full" role="img" aria-label="Photo of a blue and white striped mug filled with tea, softly blurred" style="background:linear-gradient(180deg,#6a5a3a 0%,#8c6a40 35%,#c9c5b8 55%,#2a4fb0 70%,#e8e8f0 80%,#2a4fb0 92%)"></div>
      <div class="tag" style="font-size:13px;line-height:20px;width:150px;left:15px"><span>May I have an another coffee ?</span></div>
      <span class="date" style="color:#d8dce8">January 28, 2013</span>
    </article>

    <article class="card">
      <div class="media" role="img" aria-label="Photo of a woman standing in an abandoned industrial hall" style="background:linear-gradient(180deg,#3a302a,#8a7a6a 50%,#4a3a2e)"></div>
      <h3>Science World</h3>
      <p>Pellentesque habitant morbi tristique senectus et netus et malesuada fames ac turpis egestas. Phasellus vel massa laoreet neque malesuada auctor ut eu augue. Vivamus vitae leo dui.</p>
      <span class="date">January 20, 2013</span>
    </article>

    <article class="card">
      <div class="media" role="img" aria-label="Black and white portrait photo of a soul singer" style="background:linear-gradient(180deg,#1a1a1a,#6a6a6a 60%,#d8d8d8)"></div>
      <h3>Singer and songwriter: Elmer Vance</h3>
      <p>Elmer Roy Vance, Jr. (March 2, 1940 – November 8, 1968) was an American singer and songwriter, record producer, arranger and talent scout.</p>
      <span class="date">December 24, 2012</span>
    </article>

    <article class="card">
      <div class="media" role="img" aria-label="Abstract colourful geometric artwork in red, purple and yellow" style="background:linear-gradient(135deg,#0a0a1a 10%,#6a1a6a 40%,#d8283a 60%,#f0b020 78%,#1a1a3a)"></div>
      <h3>An awesome image gallery</h3>
      <p>Suspendisse auctor dui non ligula suscipit sit amet congue dolor tempus. Suspendisse varius, nisl ut vulputate pellentesque, neque risus hendrerit risus.</p>
      <span class="date">November 18, 2012</span>
    </article>
  </div>
</main>

<footer class="site-footer">
  <div class="footer-col" style="left:87px"><h4>Say hello</h4><a href="#" style="margin-left:-33px">e-mail: hello@vexilune.example</a></div>
  <div class="footer-col" style="left:365px"><h4>Call us</h4><a href="#" style="margin-left:-14px">phone: 0491 570 156</a></div>
  <div class="footer-col" style="left:643px"><h4>Follow us</h4>
    <div class="socials" aria-label="Social profiles"><span></span><span></span><span></span><span></span><span></span><span></span><span></span></div>
  </div>
</footer>
</body>
</html>
```